Kindled Poster

I need a poster for a television show. The poster would be used primarily online and I want it to be rectangle to mirror 16:9 TV aspect ratio. The name of the program is “Kindled” (logo attached). “Kindled” will be a 30 minute weekly show that features interviews from all walks of life of how the transforming power of God has changed lives. I want the logo to be included on the poster, and little section left open so I can add pictures of people that will share their story for each episode. The text should also include “Larkfield rtv” logo (TV station producing show), name of producer and where the show can be viewed.
Tv

```html
<!DOCTYPE html>
<html lang="en">
<head>
<meta charset="utf-8">
<title>Kindled Poster</title>
<link href="https://fonts.googleapis.com/css2?family=Jura:wght@300;700&display=swap" rel="stylesheet">
<style>
  :root {
    --page: #ffffff;
    --night: #020101;
    --dusk: #0d0303;
    --ember: #2a0504;
    --glow: #3a120a;
    --title: #e9e9e9;
    --title-key: #ffffff;
    --accent: #c8141b;
    --skin-light: #c49a7e;
    --skin-mid: #a47a60;
    --skin-dark: #6e4a36;
  }
  html, body {
    margin: 0;
    padding: 0;
    overflow: hidden;
    background: var(--page);
  }
  .canvas {
    position: relative;
    width: 1200px;
    height: 1000px;
    background: var(--page);
    overflow: hidden;
  }
  .banner {
    position: absolute;
    left: 10px;
    top: 168px;
    width: 1180px;
    height: 664px;
    overflow: hidden;
  }
  .backdrop {
    position: absolute;
    inset: 0;
    background:
      radial-gradient(ellipse 460px 300px at 360px 330px, var(--night) 45%, transparent 100%),
      radial-gradient(ellipse 700px 120px at 420px 0px, var(--glow) 0%, transparent 100%),
      radial-gradient(ellipse 700px 120px at 420px 664px, var(--glow) 0%, transparent 100%),
      linear-gradient(90deg, var(--night) 0%, var(--dusk) 55%, var(--ember) 100%);
  }
  .guest-portrait {
    position: absolute;
    left: 785px;
    top: 54px;
    width: 395px;
    height: 558px;
    background: radial-gradient(ellipse 240px 300px at 60% 40%, var(--skin-light) 0%, var(--skin-mid) 55%, var(--skin-dark) 100%);
    border-radius: 60px 0 0 30px;
  }
  .show-title {
    position: absolute;
    left: 40px;
    top: 436px;
    width: 700px;
    height: 80px;
    margin: 0;
  }
  .show-title .letter {
    position: absolute;
    top: 0;
    width: 40px;
    font-family: "Jura", sans-serif;
    font-weight: 300;
    font-size: 38px;
    line-height: 40px;
    text-align: center;
    color: var(--title);
  }
  .show-title .echo {
    position: absolute;
    left: 0;
    top: 34px;
    width: 40px;
    transform: scaleY(-1);
    opacity: 0.3;
    -webkit-mask-image: linear-gradient(to top, #000 0%, transparent 60%);
    mask-image: linear-gradient(to top, #000 0%, transparent 60%);
  }
  .show-title .letter.is-key {
    font-weight: 700;
    color: var(--title-key);
    text-shadow: 0 0 6px rgba(255,255,255,0.6);
  }
  .show-title .letter.is-key .echo {
    color: var(--accent);
    opacity: 0.95;
    text-shadow: none;
  }
  .station-name {
    position: absolute;
    left: 318px;
    top: 555px;
    font-family: "Jura", sans-serif;
    font-weight: 700;
    font-size: 21px;
    line-height: 24px;
    color: var(--title-key);
    display: flex;
    align-items: center;
    gap: 6px;
  }
  .station-name .mark {
    width: 10px;
    height: 10px;
    background: var(--title-key);
  }
  .station-echo {
    top: 581px;
    transform: scaleY(-1);
    opacity: 0.3;
    -webkit-mask-image: linear-gradient(to top, #000 0%, transparent 70%);
    mask-image: linear-gradient(to top, #000 0%, transparent 70%);
  }
</style>
</head>
<body>
<main class="canvas">
  <section class="banner">
    <div class="backdrop" role="img" aria-label="Dark background with soft out-of-focus coloured lights"></div>
    <div class="guest-portrait" role="img" aria-label="Close-up photo of the episode's featured guest in profile, speaking"></div>
  </section>

  <h1 class="show-title" aria-label="Kindled">
    <span class="letter" style="left:0px">K<span class="echo" aria-hidden="true">K</span></span>
    <span class="letter" style="left:107px">I<span class="echo" aria-hidden="true">I</span></span>
    <span class="letter" style="left:212px">N<span class="echo" aria-hidden="true">N</span></span>
    <span class="letter is-key" style="left:310px">D<span class="echo" aria-hidden="true">D</span></span>
    <span class="letter" style="left:414px">L<span class="echo" aria-hidden="true">L</span></span>
    <span class="letter" style="left:518px">E<span class="echo" aria-hidden="true">E</span></span>
    <span class="letter" style="left:624px">D<span class="echo" aria-hidden="true">D</span></span>
  </h1>

  <div class="station-name"><span class="mark" aria-hidden="true"></span>Larkfield rtv</div>
  <div class="station-name station-echo" aria-hidden="true"><span class="mark"></span>Larkfield rtv</div>
</main>
</body>
</html>
```